依頼詳細
写真挿入は無し、メニュー、営業時間も別看板がありますので記載不要です。添付のロゴとイラストを挿入してください。看板は両面ですが1デザインでも構いません。
記載項目
記載項目
⚪店名 月灯りこまち
⚪定食 お酒 または、お食事 呑み処 など(デザインとのバランスでお願いします。)
⚪お気軽にどうぞ、気軽に来店ください など(安心して気軽に入店しやすくなる1フレーズ)
⚪イラストにふき出しで発声させてください。(フレーズはお任せします。)
⚪サイズは450mm×1300mmで縦長です。納品はaiデータです。
⚪文字色、全体的なデザインはお任せですが、背景色は薄ピンクが希望色です。グラデーションも好きです。イラスト、ロゴとのバランスでお願いします。
希望イメージ
シンプル 複雑
単色 カラフル
暗い 明るい
日常 高級
遊び心 厳粛
未来的 伝統的
女性的 男性的
希望する色
納品ファイル
• イラストレーター形式 (.ai)
補足説明
私ai使えませんので確認は別形式でお願いします。
選定確約有りに変更しました。

見やすくバランスが良く丁度良いです。

また、よろしくお願いいたします。

```html
<!DOCTYPE html>
<html lang="ja">
<head>
<meta charset="utf-8">
<title>月灯りこまち のぼり</title>
<link rel="stylesheet" href="https://fonts.googleapis.com/css2?family=Yuji+Syuku&family=Shippori+Mincho+B1:wght@700&family=Zen+Maru+Gothic:wght@500&display=swap">
<style>
  :root {
    --bg-light: #fdeef3;
    --bg-pink: #f6c9d8;
    --bg-deep: #efb0c6;
    --glow: rgba(255, 255, 255, 0.85);
    --ink: #1d1418;
    --name-brown: #8c5a2e;
    --roman: #6b4a2c;
    --bubble-fill: #ffffff;
    --bubble-line: #4a2e52;
    --bubble-ink: #3a2444;
    --figure-pink: #f2a9c5;
    --figure-rose: #e783aa;
    --figure-green: #9cc086;
    --figure-white: #fbfbf6;
  }
  * { margin: 0; padding: 0; box-sizing: border-box; }
  html, body { width: 1200px; height: 2970px; overflow: hidden; }
  body { background: var(--bg-light); }

  .banner {
    position: relative;
    width: 1200px;
    height: 2970px;
    overflow: hidden;
    background:
      radial-gradient(ellipse 520px 460px at 560px 760px, var(--glow), transparent 70%),
      radial-gradient(ellipse 700px 600px at 1050px 300px, rgba(239,176,198,0.55), transparent 70%),
      radial-gradient(ellipse 700px 700px at 150px 1900px, rgba(239,176,198,0.45), transparent 70%),
      linear-gradient(180deg, var(--bg-pink) 0%, var(--bg-light) 35%, var(--bg-pink) 70%, var(--bg-deep) 100%);
  }

  .category {
    position: absolute;
    top: 40px;
    right: 200px;
    writing-mode: vertical-rl;
    font-family: "Yuji Syuku", serif;
    font-size: 92px;
    line-height: 1;
    letter-spacing: 6px;
    color: var(--ink);
  }
  .category .gap { display: inline-block; height: 46px; }

  .shop-name {
    position: absolute;
    top: 170px;
    left: 190px;
    font-family: "Yuji Syuku", serif;
    font-weight: 400;
    color: var(--name-brown);
    font-size: 200px;
    line-height: 1.25;
    white-space: nowrap;
  }
  .shop-name .line { display: block; }
  .shop-name .line-2 { padding-left: 70px; }

  .shop-roman {
    position: absolute;
    top: 810px;
    left: 830px;
    font-family: "Zen Maru Gothic", sans-serif;
    font-size: 46px;
    line-height: 1.15;
    color: var(--roman);
    letter-spacing: 2px;
  }

  .mascot {
    position: absolute;
    left: 590px;
    top: 1030px;
    width: 560px;
    height: 1880px;
    border-radius: 280px 280px 120px 120px;
    background: linear-gradient(180deg,
      var(--figure-pink) 0%,
      var(--figure-green) 32%,
      var(--figure-rose) 48%,
      var(--figure-rose) 70%,
      var(--figure-green) 84%,
      var(--figure-white) 100%);
    opacity: 0.9;
  }

  .speech {
    position: absolute;
    left: 100px;
    top: 1110px;
    width: 540px;
    height: 1440px;
  }
  .speech svg { position: absolute; inset: 0; }
  .speech-text {
    position: absolute;
    top: 110px;
    left: 70px;
    width: 360px;
    height: 1220px;
    writing-mode: vertical-rl;
    font-family: "Shippori Mincho B1", serif;
    font-weight: 700;
    font-size: 112px;
    line-height: 1.55;
    letter-spacing: 16px;
    color: var(--bubble-ink);
  }
</style>
</head>
<body>
  <main class="banner">
    <p class="category">お食事<span class="gap"></span>呑み処</p>

    <h1 class="shop-name">
      <span class="line line-1">月灯り</span>
      <span class="line line-2">こまち</span>
    </h1>
    <p class="shop-roman">tsukiakari<br>komachi</p>

    <div class="mascot" role="img" aria-label="着物と袴姿のピンク髪の看板娘イラスト"></div>

    <div class="speech">
      <svg width="540" height="1440" viewBox="0 0 540 1440" aria-hidden="true">
        <path d="M80 12 H420 Q470 12 470 62 V90 L532 118 L470 150 V1378 Q470 1428 420 1428 H80 Q30 1428 30 1378 V62 Q30 12 80 12 Z"
              fill="var(--bubble-fill)" stroke="var(--bubble-line)" stroke-width="12" stroke-linejoin="round"/>
      </svg>
      <p class="speech-text">いちげんさま大歓迎<br>気軽に来店ください</p>
    </div>
  </main>
</body>
</html>
```